tri-fold brochure design for psychology practice - all content provided

we are a psychology practice that specialises in diagnostic and educational assessments for children, adolescents and adults. We have an existing logo and I am attaching a word doc (tri-fold brochure) with the required content. I am also attaching our logo and other relevant content docs. The layout is only a sample and we are looking for someone to put this together into a consistent and better layout.

Target Market(s)

parents

Industry/Entity Type

education and health

Font styles to use
Other font styles liked:
• crimsonpro

Requirements
Must have
• our logo and the provided content

```html
<!DOCTYPE html>
<html lang="en">
<head>
<meta charset="utf-8">
<title>Kindroot Brochure</title>
<link href="https://fonts.googleapis.com/css2?family=Crimson+Pro:wght@400;600;700&family=Open+Sans:wght@400;600;700&display=swap" rel="stylesheet">
<style>
:root{
  --bg:#e4e5e4;
  --green:#8cc63f;
  --green-dark:#5f9527;
  --green-deep:#3f6e1c;
  --green-pale:#eef6e2;
  --ink:#4a4a4a;
  --muted:#7a7a7a;
  --white:#ffffff;
  --photo-a:#c9b9a4;
  --photo-b:#e7d8c3;
}
*{box-sizing:border-box;margin:0;padding:0}
html,body{width:898px;height:1200px;overflow:hidden;background:var(--bg);font-family:"Open Sans",sans-serif;color:var(--ink)}
.sheet{position:absolute;display:flex;background:var(--white);box-shadow:0 6px 18px rgba(0,0,0,.18)}
.sheet--outside{left:60px;top:30px;width:780px;height:450px}
.sheet--inside{left:40px;top:510px;width:820px;height:640px}
.panel{position:relative;flex:1;overflow:hidden}
.panel + .panel{border-left:1px solid #e8e8e8}
.photo{background:linear-gradient(135deg,var(--photo-a),var(--photo-b))}
p{font-size:7.5px;line-height:1.55}

/* outside left: pillars */
.pillars{padding:18px 16px;display:flex;flex-direction:column;gap:10px;background:var(--green-pale);height:100%}
.pillar{background:var(--white);border-radius:4px;overflow:hidden}
.pillar__head{display:flex;align-items:center;gap:8px;background:var(--green-dark);color:var(--white);padding:6px 10px;font-weight:700;font-size:9px;letter-spacing:.08em}
.pillar__icon{width:18px;height:18px;border-radius:50%;background:var(--white);flex:none}
.pillar p{padding:8px 10px}

/* outside middle: contact */
.contact{padding:40px 22px;text-align:center}
.contact__lead{font-family:"Crimson Pro",serif;font-size:13px;line-height:1.35;color:var(--green-deep)}
.contact__btn{display:inline-block;margin:18px 0 12px;background:var(--green);color:var(--white);font-weight:700;font-size:10px;letter-spacing:.1em;padding:6px 22px;border-radius:3px}
.contact__lines p{font-size:8px}
.socials{display:flex;justify-content:center;gap:8px;margin:22px 0 10px}
.socials span{width:18px;height:18px;border-radius:50%;background:var(--green-dark)}
.contact__web{font-size:8px;font-weight:600;color:var(--green-deep)}

/* outside right: cover */
.brand{display:flex;align-items:center;gap:8px;padding:26px 20px 6px}
.brand__dot{width:24px;height:24px;border-radius:50%;background:var(--green-dark)}
.brand__name{font-family:"Crimson Pro",serif;font-weight:700;font-size:24px;color:var(--green-deep)}
.brand__tag{font-size:7px;color:var(--muted);padding-left:52px}
.cover__photo{position:absolute;left:0;right:0;top:100px;height:240px}
.cover__wave{position:absolute;left:0;bottom:0;width:100%;height:160px}
.cover__words{position:absolute;right:24px;bottom:22px;text-align:right;color:var(--white);font-family:"Crimson Pro",serif;font-size:13px;line-height:1.3}

/* inside */
.inside__photo{height:210px}
.inside__wave{position:absolute;left:0;top:170px;width:100%;height:60px}
.inside__body{position:relative;z-index:1;padding:30px 22px 14px}
.heading{font-family:"Crimson Pro",serif;font-weight:700;font-size:22px;color:var(--green-dark);margin-bottom:8px}
.kicker{font-size:8px;font-weight:700;color:var(--green-dark);margin-bottom:8px;letter-spacing:.04em}
.inside__body p{margin-bottom:8px}
.list{list-style:none;margin:4px 0 10px}
.list li{font-size:7.5px;line-height:1.7;padding-left:10px;position:relative}
.list li::before{content:"";position:absolute;left:0;top:5px;width:5px;height:5px;border-radius:50%;background:var(--green)}
.process{background:var(--green);height:100%;padding:28px 20px;color:var(--white)}
.process .heading{color:var(--white);margin-bottom:16px}
.step{display:flex;gap:10px;align-items:flex-start;margin-bottom:16px}
.step__num{flex:none;width:20px;height:20px;border-radius:50%;background:var(--white);color:var(--green-dark);font-weight:700;font-size:10px;display:flex;align-items:center;justify-content:center}
.step p{color:var(--white)}
</style>
</head>
<body>

<section class="sheet sheet--outside">
  <div class="panel">
    <div class="pillars">
      <div class="pillar"><div class="pillar__head"><span class="pillar__icon"></span>UNDERSTANDING</div>
        <p>We take time to learn about each person, their history and their goals so every assessment begins with a clear picture.</p></div>
      <div class="pillar"><div class="pillar__head"><span class="pillar__icon"></span>IDENTIFYING</div>
        <p>It is how we aim to find strengths and challenges through careful testing, observation and conversation with families.</p></div>
      <div class="pillar"><div class="pillar__head"><span class="pillar__icon"></span>GUIDING</div>
        <p>We help people to apply our findings, with practical recommendations for home, school and work settings.</p></div>
    </div>
  </div>

  <div class="panel">
    <div class="contact">
      <p class="contact__lead">We are passionate about helping people to flourish. If you or someone you love is finding learning challenging then please talk to us.</p>
      <span class="contact__btn">CONTACT US</span>
      <div class="contact__lines">
        <p>Suite 4, 12 Willow Lane</p>
        <p>Greenfield NSW 2000</p>
        <p>(02) 5550 1234</p>
        <p>hello@kindrootclinic.com.au</p>
      </div>
      <div class="socials"><span></span><span></span><span></span></div>
      <p class="contact__web">www.kindrootclinic.com.au</p>
    </div>
  </div>

  <div class="panel">
    <div class="brand"><span class="brand__dot"></span><span class="brand__name">thekindroot</span></div>
    <p class="brand__tag">diagnostic and educational assessments</p>
    <div class="cover__photo photo" role="img" aria-label="Photo of smiling children outdoors"></div>
    <svg class="cover__wave" viewBox="0 0 260 160" preserveAspectRatio="none" aria-hidden="true">
      <path d="M0 60 Q130 10 260 40 L260 160 L0 160 Z" fill="var(--green)"/>
      <path d="M0 85 Q130 40 260 70 L260 160 L0 160 Z" fill="var(--green-dark)"/>
    </svg>
    <div class="cover__words">Understanding<br>Identifying<br>Guiding</div>
  </div>
</section>

<section class="sheet sheet--inside">
  <div class="panel">
    <div class="inside__photo photo" role="img" aria-label="Photo of a psychologist working with a child at a table"></div>
    <svg class="inside__wave" viewBox="0 0 273 60" preserveAspectRatio="none" aria-hidden="true">
      <path d="M0 30 Q140 0 273 25 L273 60 L0 60 Z" fill="var(--white)"/>
      <path d="M0 30 Q140 0 273 25" fill="none" stroke="var(--green)" stroke-width="3"/>
    </svg>
    <div class="inside__body">
      <h2 class="heading">who we are</h2>
      <p class="kicker">THEKINDROOT IS A TEAM WITH A PASSION FOR HELPING PEOPLE TO THRIVE</p>
      <p>We are a team of psychologists and teachers with many years of experience in both educational and clinical settings.</p>
      <p>We understand the challenges parents face in seeking answers and support for their children, and we work to make the process clear and caring.</p>
      <p>We are passionate about working to help families recognise the strengths and needs of each person, and we deliver thorough, easy to read reports.</p>
      <p>We work collaboratively with other professionals to ensure that recommendations and supports are in place at home, at school and beyond.</p>
    </div>
  </div>

  <div class="panel">
    <div class="inside__photo photo" role="img" aria-label="Photo of a child reading with an adult"></div>
    <svg class="inside__wave" viewBox="0 0 273 60" preserveAspectRatio="none" aria-hidden="true">
      <path d="M0 25 Q140 0 273 30 L273 60 L0 60 Z" fill="var(--white)"/>
      <path d="M0 25 Q140 0 273 30" fill="none" stroke="var(--green)" stroke-width="3"/>
    </svg>
    <div class="inside__body">
      <p>We are qualified to give formal diagnoses and conduct a wide range of standard assessments. We offer:</p>
      <ul class="list">
        <li>Attention Deficit Hyperactivity Disorder</li>
        <li>Autism Spectrum Disorder</li>
        <li>Specific Learning Disorder</li>
        <li>Language Disorders</li>
        <li>Anxiety Disorders</li>
        <li>Mood Disorders</li>
        <li>Intellectual Disability</li>
      </ul>
      <p>We are passionate about collaborating with your child's school and other professionals, supporting them to apply the recommendations in our reports.</p>
      <p>We also provide follow up sessions to help families understand results and plan the next steps with confidence.</p>
    </div>
  </div>

  <div class="panel">
    <div class="process">
      <h2 class="heading">the process</h2>
      <div class="step"><span class="step__num">1</span><p>An initial phone call to discuss your concerns and determine the most suitable type of assessment.</p></div>
      <div class="step"><span class="step__num">2</span><p>A parent interview to gather background information, developmental history and current concerns in detail.</p></div>
      <div class="step"><span class="step__num">3</span><p>Gathering additional information from teachers and other professionals through questionnaires and reports.</p></div>
      <div class="step"><span class="step__num">4</span><p>Assessment sessions with your child, using standardised tests in a calm and friendly environment.</p></div>
      <div class="step"><span class="step__num">5</span><p>A feedback session to explain the findings, followed by a written report with practical recommendations.</p></div>
    </div>
  </div>
</section>

</body>
</html>
```